Community Harvest Festival Poster

Seeking a poster design to advertise our community’s annual Harvest Festival. We will utilize and display printed posters as well as distribute PDFs via our weekly e-news letters. This years "theme" is, "Copper Lantern/Maple Ridge Fair, Where City and Country Meet." The vibe is a bohemian, beatnik, street scene, meets a old fashioned orchard.

Target Market(s)

NYC School Community- should appeal to an audience that ranges from kids to grandparents. Very family oriented, with wide appeal, and must be eye catching.

Other font styles liked:
• One style should be more of a "Country" font, the other should have more of a clean city vibe.

Colors
acd037
ffc214
f68e4e
eaf2ce

Requirements
Must have
• The following copy:
• Copper Lantern Maple Ridge Fair
• Where City and Country Meet
• Celebrate C&C With Great Food, Music, Entertainment, And Fun!
• Saturday, October 19th 2019
• 12:00-4:00pm
• Tickets will be available for sale at Drop off and Pick up
Nice to have
• I'm not limited, but a couple of ideas that could be cool:
• One incorporated the background of a street, i.e. pavement, which has leaves blowing over it, and perhaps an apple or two rolling onto the page.
• Another has a diagonal breakup of the image, with one side pavement and the other side rustic wood, also with leaves sweeping across.
• I've also attached images of previous festival posters that I have gravitated to for some idea of quality I'm looking for.
Should not have
• Anything inappropriate for children.

```html
<!DOCTYPE html>
<html lang="en">
<head>
<meta charset="utf-8">
<title>Copper Lantern Maple Ridge Fair – Harvest Festival Poster</title>
<link rel="stylesheet" href="https://fonts.googleapis.com/css2?family=Cinzel:wght@400;500&family=Questrial&family=Montserrat:wght@600;700&family=Playball&display=swap">
<style>
  :root {
    --page-bg: #e4e4e4;
    --wood-dark: #3a0e07;
    --wood-mid: #6a2213;
    --wood-light: #84301b;
    --cream: #f4dcb5;
    --cream-soft: #f1e6d2;
    --ribbon: #ebe4d7;
    --ribbon-shade: #c9bdaa;
    --ribbon-fold: #9c8f7c;
    --ink: #2a1a12;
    --photo-sky: #a9a59c;
    --photo-facade: #6b4a33;
    --photo-stone: #4a3a2e;
    --photo-shadow: #241a14;
  }
  * { margin: 0; padding: 0; box-sizing: border-box; }
  html, body { width: 1200px; height: 848px; overflow: hidden; }
  body { background: var(--page-bg); position: relative; }

  .poster {
    position: absolute;
    left: 333px; top: 24px;
    width: 534px; height: 800px;
    overflow: hidden;
    background:
      repeating-linear-gradient(90deg, rgba(0,0,0,0.06) 0 3px, rgba(255,255,255,0.02) 3px 9px, rgba(0,0,0,0.04) 9px 17px),
      radial-gradient(ellipse at 50% 40%, var(--wood-light) 0%, var(--wood-mid) 55%, var(--wood-dark) 100%);
    box-shadow: 0 2px 6px rgba(0,0,0,0.35);
  }
  .poster-art { position: absolute; inset: 0; }

  .title {
    position: absolute; left: 0; right: 0; top: 74px;
    text-align: center;
    font-family: "Cinzel", serif;
    font-weight: 400;
    color: var(--cream);
    line-height: 1;
    text-shadow: 0 2px 3px rgba(0,0,0,0.45);
  }
  .title-line-small { display: block; font-size: 42px; }
  .title-line-large { display: block; font-size: 58px; margin-top: 2px; }
  .title-line-small.last { margin-top: 0; font-size: 44px; }

  .time {
    position: absolute; left: 126px; width: 282px; top: 246px;
    text-align: center;
    font-family: "Questrial", sans-serif;
    font-size: 30px;
    line-height: 1;
    color: var(--ink);
    letter-spacing: 1px;
  }

  .tagline {
    position: absolute; left: 0; right: 0; top: 560px;
    text-align: center;
    font-family: "Cinzel", serif;
    font-weight: 500;
    font-size: 25px;
    line-height: 1;
    color: var(--cream);
    text-shadow: 0 2px 4px rgba(0,0,0,0.85);
  }
  .tagline-rule {
    position: absolute; left: 78px; right: 78px; top: 590px;
    height: 1px; background: var(--cream); opacity: 0.8;
  }

  .celebrate {
    position: absolute; left: 0; right: 0; top: 612px;
    text-align: center;
    font-family: "Playball", cursive;
    font-size: 36px;
    line-height: 1;
    color: var(--cream);
  }
  .details {
    position: absolute; left: 0; right: 0; top: 653px;
    text-align: center;
    font-family: "Questrial", sans-serif;
    font-size: 25px;
    line-height: 30px;
    color: var(--cream-soft);
  }
  .date {
    position: absolute; left: 0; right: 0; top: 718px;
    text-align: center;
    font-family: "Montserrat", sans-serif;
    font-weight: 700;
    font-size: 22px;
    line-height: 1;
    color: var(--cream);
  }
  .tickets {
    position: absolute; left: 0; right: 0; top: 750px;
    text-align: center;
    font-family: "Questrial", sans-serif;
    font-size: 12.5px;
    color: var(--cream-soft);
    text-transform: uppercase;
  }
</style>
</head>
<body>
  <main class="poster">
    <svg class="poster-art" width="534" height="800" viewBox="0 0 534 800">
      <defs>
        <linearGradient id="street-tones" x1="0" y1="0" x2="0" y2="1">
          <stop offset="0" stop-color="var(--photo-sky)"/>
          <stop offset="0.22" stop-color="var(--photo-facade)"/>
          <stop offset="0.65" stop-color="var(--photo-stone)"/>
          <stop offset="1" stop-color="var(--photo-shadow)"/>
        </linearGradient>
        <radialGradient id="street-vignette" cx="0.5" cy="0.35" r="0.7">
          <stop offset="0.3" stop-color="#000" stop-opacity="0"/>
          <stop offset="1" stop-color="#000" stop-opacity="0.55"/>
        </radialGradient>
      </defs>
      <g class="street-photo" role="img" aria-label="Photo of an old European cobblestone street lined with historic townhouses">
        <polygon fill="url(#street-tones)"
          points="0,252 60,238 130,224 200,214 300,212 380,224 460,252 534,272 534,662 0,522"/>
        <polygon fill="url(#street-vignette)"
          points="0,252 60,238 130,224 200,214 300,212 380,224 460,252 534,272 534,662 0,522"/>
      </g>
      <g class="time-ribbon">
        <path class="ribbon-tail" d="M6,204 Q70,210 140,232 L140,276 Q74,256 14,252 L36,228 Z" fill="var(--ribbon-shade)"/>
        <path class="ribbon-tail" d="M528,204 Q464,210 394,232 L394,276 Q460,256 520,252 L498,228 Z" fill="var(--ribbon-shade)"/>
        <path class="ribbon-fold" d="M126,240 L140,232 L140,276 L126,290 Z" fill="var(--ribbon-fold)"/>
        <path class="ribbon-fold" d="M408,240 L394,232 L394,276 L408,290 Z" fill="var(--ribbon-fold)"/>
        <path class="ribbon-band" d="M126,240 Q267,222 408,240 L408,290 Q267,272 126,290 Z" fill="var(--ribbon)"/>
      </g>
    </svg>

    <h1 class="title">
      <span class="title-line-small">Copper Lantern</span>
      <span class="title-line-large">Maple Ridge</span>
      <span class="title-line-small last">Fair</span>
    </h1>

    <p class="time">12:00 - 4:00PM</p>

    <p class="tagline">WHERE CITY AND COUNTRY MEET</p>
    <div class="tagline-rule"></div>

    <p class="celebrate">Celebrate</p>
    <p class="details">C&amp;C With Great Food, Music,<br>Entertainment, And Fun!</p>
    <p class="date">SATURDAY, OCTOBER 19TH 2019</p>
    <p class="tickets">Tickets will be available for sale at drop off and pick up</p>
  </main>
</body>
</html>
```